Elegant and modern body scrub for organic junkies

I need a package design for my new company based out of Austin, Texas. We are focused on cruelty free and all natural and organic products. Our deign needs to be able to have the information we require on it, while still appearing very clean and captivating. Our initial product is a clear skin body scrub, intended for people with problematic skin. Our target market is women and we want to show elegance, without appearing "high end."
Updates

Reason: I want to allot more time for certain designers to submit edits. Last minute proposals have been appealing

Target Market(s)

Women. Organic and holistic minded. Natural beauty lovers.

Industry/Entity Type

Skin Care Product

Font styles to use
Script
Other font styles liked:
• AmericanTypewriter, Beautifulflaws, courier, caviarDreams-bold

Colors
000000
ffc214
ffffff
fece3e
fbee3e

Requirements
Must have
• Must be designed in Adobe Illustrator.
• The photo titled “structure for oz and grams” -That needs to be included at the bottom of 1B. I like the horizontal and vertical bar that separate the two. I want that.
• Color Inspiration - The photo titled “vorna color inspiration” and “color combo inspiration” are the colors I want. BLACK, GOLD, WHITE. I want the label background black and the writing in white with some gold somewhere on it. My logo is going to be a Ivory Lantern.
• The photos titled “I like how clean this looks” and “I also like how clean this looks” - I want 1B to look super clean. I don’t want a lot of information in this box. I want simple and clean. This is where the logo and brand name will go.
• Logo - A Ivory Lantern. I want it to be gold and geometric. There can be dimension like this elephant example on the left of the 1B description. I want the trunk to be facing to the left and the trunk needs to be raised overhead and touching the animal's forehead.
• The photo titled “sideways writing and silver rim” - I want 1C to be written sideways like this. My text will be much more extensive so the font won’t be able to be so big.
Nice to have
• The photo titled “sideways writing and silver rim” - I want 1C to be written sideways like this. My text will be much more extensive so the font won’t be able to be so big. I also REALLY like how this label is rimmed in silver, but I would want gold. This is not mandatory, but I really like this.
• The photo titled “melted honey” - This is another option I really like. The gold that looks like honey dripping on the label is really cool. Not mandatory, but I really liked that. I also like the craft background on this.
• Color Inspiration - The photo titled “color inspiration” and “another color inspiration” is an option I would also like to see. Rather than black, I’d like to see what it would ALSO look like with a navy background. NAVY, GOLD, WHITE, maybe black somewhere.
Should not have
• Colorful patterns or excessive info in section 1B.

```html
<!DOCTYPE html>
<html lang="en">
<head>
<meta charset="utf-8">
<title>Ivory Lantern Body Scrub Label</title>
<link href="https://fonts.googleapis.com/css2?family=Courier+Prime:wght@400;700&family=Josefin+Sans:wght@300;400&display=swap" rel="stylesheet">
<style>
  :root {
    --bg-top: #a9a9a9;
    --bg-bottom: #f2f2f2;
    --label-black: #0d0d0d;
    --gold: #c9a548;
    --ink-white: #f4f4f4;
  }
  * { margin: 0; padding: 0; box-sizing: border-box; }
  html, body { width: 1200px; height: 1040px; overflow: hidden; }
  body {
    background: linear-gradient(180deg, var(--bg-top) 0%, #d6d6d6 45%, var(--bg-bottom) 100%);
    position: relative;
  }
  .label {
    position: absolute;
    left: 40px;
    top: 350px;
    width: 1120px;
    height: 340px;
    background: var(--label-black);
    display: flex;
    border-top: 6px solid var(--gold);
    border-bottom: 6px solid var(--gold);
  }
  .label::before,
  .label::after {
    content: "";
    position: absolute;
    left: 0; right: 0;
    height: 2px;
    background: var(--gold);
  }
  .label::before { top: 10px; }
  .label::after { bottom: 10px; }

  .panel { position: relative; height: 100%; }

  .brand-mark {
    font-family: "Courier Prime", monospace;
    font-weight: 400;
    font-size: 26px;
    line-height: 1.3;
    letter-spacing: 2px;
    color: var(--gold);
    text-align: center;
    white-space: nowrap;
  }

  /* Front panel: mark + brand */
  .panel-front {
    width: 610px;
    display: flex;
    align-items: center;
    padding: 0 30px 0 40px;
    gap: 30px;
  }
  .panel-front .brand-mark { width: 150px; flex-shrink: 0; }
  .brand-block { flex: 1; color: var(--ink-white); white-space: nowrap; }
  .brand-name {
    font-family: "Courier Prime", monospace;
    font-weight: 700;
    font-size: 24px;
    letter-spacing: 1px;
    padding-bottom: 10px;
  }
  .product-row {
    display: flex;
    border-top: 1.5px solid var(--ink-white);
    border-bottom: 1.5px solid var(--ink-white);
    font-family: "Courier Prime", monospace;
    font-size: 22px;
  }
  .product-type { width: 180px; padding: 12px 0; border-right: 1.5px solid var(--ink-white); }
  .product-year { padding: 12px 0 12px 22px; }
  .claim {
    font-family: "Courier Prime", monospace;
    font-weight: 700;
    font-size: 22px;
    padding: 14px 0 10px;
    border-bottom: 1.5px solid var(--ink-white);
  }
  .tagline {
    font-family: "Josefin Sans", sans-serif;
    font-weight: 300;
    font-size: 14px;
    padding-top: 10px;
  }

  /* Info panel: sideways text */
  .panel-info {
    width: 320px;
    display: flex;
    justify-content: center;
    align-items: center;
    padding: 24px 0;
  }
  .sideways {
    writing-mode: vertical-rl;
    transform: rotate(180deg);
    height: 290px;
    font-family: "Josefin Sans", sans-serif;
    font-weight: 300;
    font-size: 12.5px;
    line-height: 1.55;
    color: var(--ink-white);
    text-align: justify;
  }
  .sideways p + p { margin-right: 12px; }

  /* Back panel: repeated name */
  .panel-back {
    flex: 1;
    display: flex;
    align-items: center;
    justify-content: center;
  }
</style>
</head>
<body>
  <div class="label">
    <section class="panel panel-front">
      <p class="brand-mark">IVORY<br>LANTERN</p>
      <div class="brand-block">
        <h1 class="brand-name">IVORY LANTERN</h1>
        <div class="product-row">
          <span class="product-type">body scrub</span>
          <span class="product-year">1989</span>
        </div>
        <p class="claim">For problematic skin</p>
        <p class="tagline">Handmade in small batches with Love</p>
      </div>
    </section>

    <section class="panel panel-info">
      <div class="sideways">
        <p>This gentle scrub blends mineral salts with nourishing oils and pure essential oils to calm the skin, lift away dull cells, clear the pores and help prevent future breakouts.</p>
        <p>Each of these ingredients plays an essential role in anti aging as well as fighting problematic skin. Use this skin polish regularly to receive prime results.</p>
        <p>Ingredients: Dead Sea Salt, Pink Himalayan Salt, Coconut oil, Argan Oil, Jojoba Oil, Almond Oil, Lavender EO, Tea Tree EO, Geranium EO, Chamomile EO, Frankincense EO, Bergamot EO, Rosemary EO.</p>
      </div>
    </section>

    <section class="panel panel-back">
      <p class="brand-mark">IVORY<br>LANTERN</p>
    </section>
  </div>
</body>
</html>
```